Flyer for customer acquisition.

Hello, We are a sportmanagement agency from Germany and we need information flyers for customer acquisition. It should be DinA4 and should have a modern but serious design. I have uploaded a information sheet, where you can find the text and the composition, the flyer should have. I also uploaded Pictures / Images, which you can use. Of course you can use other suitable images. If they are not free, I will buy them later. On the bottom of the flyer there has been the contact information. You will find them in the download section, too. If you have questions, just write me. If I forgot something, I will update the letter :) Thank you very much!
Ich brauche zusätzliche Tage um durchzusehen

```html
<!DOCTYPE html>
<html lang="de">
<head>
<meta charset="utf-8">
<title>NVK – Nachwuchs Flyer</title>
<link rel="stylesheet" href="https://fonts.googleapis.com/css2?family=Archivo+Black&family=Raleway:wght@400;500&display=swap">
<style>
  :root {
    --page-bg: #4a4a4a;
    --blue-deep: #1f86c2;
    --blue-mid: #3aa2d8;
    --blue-pale: #d9eef9;
    --ink: #111111;
    --white: #ffffff;
    --footer: #050505;
    --icon-blue: #3fb0e6;
  }
  * { box-sizing: border-box; margin: 0; padding: 0; }
  html, body { width: 1200px; height: 1200px; overflow: hidden; }
  body { background: var(--page-bg); position: relative; font-family: "Raleway", sans-serif; }

  .flyer {
    position: absolute; left: 186px; top: 20px;
    width: 828px; height: 1160px; overflow: hidden;
    background: linear-gradient(180deg, var(--blue-deep) 15%, var(--blue-mid) 60%, var(--blue-pale) 82%, var(--white) 94%);
  }
  .flyer-shapes { position: absolute; inset: 0; }

  .brand {
    position: absolute; left: 0; top: 70px; width: 350px; text-align: center;
    font-family: "Archivo Black", sans-serif; font-size: 40px; color: var(--ink); letter-spacing: 1px;
  }
  .brand-dot {
    display: block; width: 46px; height: 46px; margin: 0 auto 10px;
    border: 3px solid var(--ink); border-radius: 50%;
  }

  .team-photo {
    position: absolute; left: 618px; top: 256px; width: 192px; height: 192px;
    border-radius: 50%; border: 5px solid var(--ink);
    background: radial-gradient(circle at 50% 40%, #d8d8d8, #7a7a7a 70%, #3a3a3a);
    box-shadow: 0 0 0 3px var(--white) inset;
  }

  .hero-title { position: absolute; left: 26px; top: 278px; color: var(--white); font-family: "Archivo Black", sans-serif; }
  .hero-title .brand-line { color: var(--ink); font-size: 46px; line-height: 1.05; }
  .hero-title .headline { font-size: 42px; line-height: 1.12; margin-top: 4px; }
  .hero-title .tagline { font-size: 22px; margin-top: 8px; }

  .services { position: absolute; left: 19px; top: 483px; width: 800px; }
  .service { position: absolute; width: 384px; }
  .service h2 {
    font-family: "Archivo Black", sans-serif; font-size: 18px; font-weight: 400; color: var(--ink);
    display: flex; align-items: center; gap: 6px; margin-bottom: 4px;
  }
  .service h2 svg { width: 20px; height: 18px; flex: none; }
  .service p {
    margin-left: 25px; font-size: 14px; line-height: 19.5px; color: var(--white);
    text-align: justify; hyphens: manual;
  }
  .col-left { left: 0; }
  .col-right { left: 399px; }
  .row-1 { top: 0; } .row-2 { top: 124px; } .row-3 { top: 230px; }

  .footnotes { position: absolute; left: 28px; top: 832px; width: 770px; font-size: 11px; line-height: 14.5px; color: var(--white); }
  .footnotes p + p { margin-top: 10px; }

  .chess-art {
    position: absolute; left: 138px; top: 905px; width: 553px; height: 187px;
    background: linear-gradient(180deg, rgba(58,162,216,0) 0%, rgba(58,162,216,0.55) 35%, rgba(45,150,210,0.8) 100%);
  }

  .contact-bar {
    position: absolute; left: 0; bottom: 0; width: 828px; height: 68px; background: var(--footer);
    color: var(--white); font-size: 18px; font-weight: 500;
  }
  .contact-item { position: absolute; top: 21px; display: flex; align-items: center; gap: 8px; }
  .contact-item svg { width: 26px; height: 26px; }
  .contact-phone { left: 27px; } .contact-mail { left: 309px; } .contact-web { left: 604px; }
</style>
</head>
<body>
<main class="flyer">
  <svg class="flyer-shapes" viewBox="0 0 828 1160" preserveAspectRatio="none">
    <defs>
      <linearGradient id="pitchTones" x1="0" y1="0" x2="0" y2="1">
        <stop offset="0" stop-color="#3b4866"/>
        <stop offset="0.5" stop-color="#8a6f6a"/>
        <stop offset="1" stop-color="#2f5a3a"/>
      </linearGradient>
    </defs>
    <polygon points="0,0 457,0 262,239 0,173" fill="#ffffff"/>
    <polygon points="457,0 828,0 828,407 262,239" fill="url(#pitchTones)" role="img" aria-label="Photo: young footballers competing for the ball in a floodlit stadium"/>
    <polyline points="0,173 262,239 828,407" fill="none" stroke="#111" stroke-width="6"/>
    <line x1="457" y1="0" x2="262" y2="239" stroke="#111" stroke-width="6"/>
  </svg>

  <div class="brand"><span class="brand-dot"></span>NVK</div>

  <div class="team-photo" role="img" aria-label="Photo: the three agency managers in dark suits"></div>

  <header class="hero-title">
    <div class="brand-line">NVK</div>
    <h1 class="headline">Nachwuch förderung<br>und -mangement</h1>
    <div class="tagline">Wir begleiten dich auf deinem Weg zum Profi</div>
  </header>

  <section class="services">
    <article class="service col-left row-1">
      <h2><svg viewBox="0 0 20 18"><rect x="1" y="4" width="13" height="13" fill="none" stroke="#111" stroke-width="2"/><path d="M4 9l4 4 10-12" fill="none" stroke="#111" stroke-width="2.5"/></svg>Karriereplanung</h2>
      <p>Wir haben deine Karriere im Blick! In enger Absprache mit deinen Eltern und dir leiten wir die richtigen Maßnahmen und Schritte ein, um dein Ziel „Profifußballer“ zu realisieren.</p>
    </article>
    <article class="service col-right row-1">
      <h2><svg viewBox="0 0 20 18"><rect x="1" y="4" width="13" height="13" fill="none" stroke="#111" stroke-width="2"/><path d="M4 9l4 4 10-12" fill="none" stroke="#111" stroke-width="2.5"/></svg>Ausrüstung</h2>
      <p>Wir besorgen dir deine Ausrüstung! Unsere Bezie&shy;hungen zu den großen Sportartikel&shy;herstellern er&shy;möglichen den Abschluss von Ausrüster&shy;verträgen*.</p>
    </article>
    <article class="service col-left row-2">
      <h2><svg viewBox="0 0 20 18"><rect x="1" y="4" width="13" height="13" fill="none" stroke="#111" stroke-width="2"/><path d="M4 9l4 4 10-12" fill="none" stroke="#111" stroke-width="2.5"/></svg>Ständiger Ansprechpartner</h2>
      <p>Egal um welchen Themen es sich handelt, wir sind für dich da! Ein vertrauensvolles und freund&shy;schaftliches Verhältnis ist uns besonders wichtig.</p>
    </article>
    <article class="service col-right row-2">
      <h2><svg viewBox="0 0 20 18"><rect x="1" y="4" width="13" height="13" fill="none" stroke="#111" stroke-width="2"/><path d="M4 9l4 4 10-12" fill="none" stroke="#111" stroke-width="2.5"/></svg>Vorsorge</h2>
      <p style="text-align:left">Verletzungen gehören leider zum Fußball dazu.<br>Wir sichern dich ab, indem wir eine private Zusatz&shy;krankenversicherung für dich abschließen.</p>
    </article>
    <article class="service col-left row-3">
      <h2><svg viewBox="0 0 20 18"><rect x="1" y="4" width="13" height="13" fill="none" stroke="#111" stroke-width="2"/><path d="M4 9l4 4 10-12" fill="none" stroke="#111" stroke-width="2.5"/></svg>Rechtsberatung/Vertragsrecht</h2>
      <p>Juristendeutsch und Kleingedrucktes?<br>Kein Problem! Wir helfen dir den Durchblick zu behalten und holen immer das Beste für dich raus.</p>
    </article>
    <article class="service col-right row-3">
      <h2><svg viewBox="0 0 20 18"><rect x="1" y="4" width="13" height="13" fill="none" stroke="#111" stroke-width="2"/><path d="M4 9l4 4 10-12" fill="none" stroke="#111" stroke-width="2.5"/></svg>Kooperationspartner/Netzwerk</h2>
      <p>Ob Entscheidungsträger oder Experte, wir kennen die richtigen Leute. Zusätzlich bieten wir dir eine große Bandbreite an Leistungen, die du jederzeit in Anspruch nehmen kannst**.</p>
    </article>
  </section>

  <footer class="footnotes">
    <p>*Die Entscheidung über das Zustandekommen eines Ausrüstervertrags obliegt dem jeweiligen Sportartikelhersteller. Ist ein Abschluss aktuell nicht möglich, erhältst du von uns 2x pro Saison neue Fußballschuhe sowie weitere Ausrüstungsgegenstände.</p>
    <p>**Personal Training, Athletik-Training, Ernährungsberatung, Sportpsychologische Betreuung, uvm.</p>
  </footer>

  <div class="chess-art" role="img" aria-label="Illustration: row of blue chess pieces as a symbol of career strategy"></div>

  <div class="contact-bar">
    <div class="contact-item contact-phone">
      <svg viewBox="0 0 26 26"><circle cx="13" cy="13" r="11.5" fill="none" stroke="var(--icon-blue)" stroke-width="2"/><path d="M9 7.5c-1 1-1 3 .5 5.5s3.5 4.5 5.5 5.5c1.5.6 2.5.2 3.2-.6l-2.2-2.2-1.5.8c-1-.5-2.5-2-3-3l.8-1.5L10.2 7z" fill="var(--icon-blue)"/></svg>
      0711/5550123
    </div>
    <div class="contact-item contact-mail">
      <svg viewBox="0 0 26 26"><rect x="2" y="7" width="22" height="14" fill="var(--icon-blue)"/><path d="M2 7l11 8 11-8" fill="none" stroke="#fff" stroke-width="1.5"/></svg>
      info@nvk-sport.de
    </div>
    <div class="contact-item contact-web">
      <svg viewBox="0 0 26 26"><circle cx="12" cy="12" r="10" fill="none" stroke="var(--icon-blue)" stroke-width="2"/><ellipse cx="12" cy="12" rx="4.5" ry="10" fill="none" stroke="var(--icon-blue)" stroke-width="1.5"/><path d="M2 12h20M4 7h16M4 17h16" stroke="var(--icon-blue)" stroke-width="1.5"/></svg>
      www.nvk-sport.de
    </div>
  </div>
</main>
</body>
</html>
```